Sole Relationship Graphic of Chapter Organization for Book

This design shows relationships between variables associated with footwear and footprints. It will be used as a graphic in a book. The four elements of the graphic are (1) Variables, (2) Book Chapter Numbers (which correspond to the relationship(s) between at least two variables, (3) Relationship Arrows, and (4) Influence Arrows (because the influencers affect the variables differently than relationships between the variables). These names simply relate to the attempts I have made (and attached) at creating a graphic. In the attached diagrams, the circles with numbers are placeholders for the book chapter numbers, which may be changed so it will be good if I can change those after the graphic is completed. Chapter 1 will be the introduction.
The intent of of outsourcing this project is not necessarily sticking to the formats I have attached, but to allow your creativity to produce a useful graphic that can visually make the most sense of the relationships between the variables as chapters to readers of the book.

Target Market(s)

Search and Rescue Trackers

Requirements
Must have
• Information listed in project description, and drafted in attached diagrams
Nice to have
• Can include outlines of barefoot and outsoles. While Chapters 1 (Intro), 2 (Missing Persons' Footwear), 10 (Case Studies) and 11 (Summary) are set, the others aren't. The end game of this book is to use the rest of the variables to arrive at the end game, which is measurements for barefoot track length or outsole track length...so those two variables can be highlighted in some way to emphasize their importance.

```html
<!DOCTYPE html>
<html lang="en">
<head>
<meta charset="utf-8">
<title>Footwear and Footprint Variables – Chapter Map</title>
<link rel="stylesheet" href="https://fonts.googleapis.com/css2?family=Comfortaa:wght@400;500&display=swap">
<style>
  :root {
    --teal: #42bfb1;
    --blue: #3f56a6;
    --orange: #f5821f;
    --paper: #ffffff;
    --ink-light: #ffffff;
  }
  html, body {
    margin: 0;
    padding: 0;
    overflow: hidden;
    background: var(--paper);
  }
  .canvas {
    width: 943px;
    height: 1200px;
    display: block;
  }
  .node { fill: var(--teal); }
  .node-label {
    fill: var(--ink-light);
    font-family: "Comfortaa", sans-serif;
    font-size: 50px;
    font-weight: 400;
    text-anchor: middle;
  }
  .node-label.small { font-size: 41px; }
  .node-label.large { font-size: 55px; }
  .rel, .inf {
    fill: none;
    stroke-width: 10;
    stroke-linecap: round;
    stroke-linejoin: round;
  }
  .rel { stroke: var(--blue); }
  .inf { stroke: var(--orange); }
  .badge-rel { fill: var(--blue); }
  .badge-inf { fill: var(--orange); }
  .badge-key { fill: var(--teal); }
  .badge-num {
    fill: var(--ink-light);
    font-family: "Comfortaa", sans-serif;
    font-size: 44px;
    font-weight: 500;
    text-anchor: middle;
    dominant-baseline: central;
  }
  .brace { fill: var(--teal); }
  .legend-frame {
    fill: none;
    stroke: var(--teal);
    stroke-width: 9;
  }
  .legend-tab { fill: var(--teal); }
  .legend-title {
    fill: var(--ink-light);
    font-family: "Comfortaa", sans-serif;
    font-size: 46px;
    font-weight: 400;
    text-anchor: middle;
  }
  .legend-text {
    font-family: "Comfortaa", sans-serif;
    font-size: 42px;
    font-weight: 400;
  }
  .legend-text.key { fill: var(--teal); font-size: 47px; }
  .legend-text.rel-text { fill: var(--blue); }
  .legend-text.inf-text { fill: var(--orange); }
</style>
</head>
<body>
<svg class="canvas" viewBox="0 0 1700 2163" xmlns="http://www.w3.org/2000/svg" role="img" aria-label="Diagram of footwear and footprint variables with chapter numbers">

  <!-- Legend -->
  <g class="legend">
    <rect class="legend-frame" x="1025" y="180" width="582" height="313" rx="22"/>
    <rect class="legend-tab" x="1190" y="150" width="252" height="62" rx="22"/>
    <text class="legend-title" x="1316" y="198" textLength="162" lengthAdjust="spacingAndGlyphs">LEGEND</text>
    <circle class="badge-key" cx="1103" cy="270" r="31"/>
    <text class="badge-num" x="1103" y="270">1</text>
    <text class="legend-text key" x="1150" y="290" textLength="225" lengthAdjust="spacingAndGlyphs">CHAPTER #</text>
    <line class="rel" x1="1115" y1="356" x2="1198" y2="357"/>
    <polyline class="rel" points="1172,330 1200,357 1172,384"/>
    <text class="legend-text rel-text" x="1220" y="373" textLength="310" lengthAdjust="spacingAndGlyphs">RELATIONSHIP TO</text>
    <line class="inf" x1="1115" y1="431" x2="1198" y2="432"/>
    <polyline class="inf" points="1172,405 1200,432 1172,459"/>
    <text class="legend-text inf-text" x="1220" y="449" textLength="255" lengthAdjust="spacingAndGlyphs">INFLUENCE ON</text>
  </g>

  <!-- Missing persons' footwear and its brace -->
  <ellipse class="node" cx="625" cy="467" rx="213" ry="133"/>
  <text class="node-label large" x="618" y="425" textLength="203" lengthAdjust="spacingAndGlyphs">MISSING</text>
  <text class="node-label large" x="618" y="488" textLength="240" lengthAdjust="spacingAndGlyphs">PERSONS’</text>
  <text class="node-label large" x="625" y="550" textLength="283" lengthAdjust="spacingAndGlyphs">FOOTWEAR</text>
  <path class="brace" d="M332,783 C350,710 385,670 435,667 L540,675 C585,678 610,650 625,612 C642,655 675,712 740,712 L825,705 C880,702 912,740 917,783 C895,728 870,710 825,711 L740,720 C675,726 640,690 625,640 C610,690 575,725 520,722 L410,716 C380,715 355,740 332,783 Z"/>

  <!-- Variables -->
  <ellipse class="node" cx="312" cy="908" rx="150" ry="93"/>
  <text class="node-label" x="312" y="902" textLength="193" lengthAdjust="spacingAndGlyphs">OUTSOLE</text>
  <text class="node-label" x="317" y="955" textLength="162" lengthAdjust="spacingAndGlyphs">LENGTH</text>

  <ellipse class="node" cx="996" cy="908" rx="150" ry="93"/>
  <text class="node-label" x="991" y="902" textLength="142" lengthAdjust="spacingAndGlyphs">INSOLE</text>
  <text class="node-label" x="996" y="955" textLength="163" lengthAdjust="spacingAndGlyphs">LENGTH</text>

  <ellipse class="node" cx="1434" cy="908" rx="150" ry="93"/>
  <text class="node-label" x="1434" y="902" textLength="127" lengthAdjust="spacingAndGlyphs">HOOK</text>
  <text class="node-label" x="1440" y="955" textLength="100" lengthAdjust="spacingAndGlyphs">AREA</text>

  <ellipse class="node" cx="565" cy="1205" rx="150" ry="93"/>
  <text class="node-label" x="563" y="1197" textLength="221" lengthAdjust="spacingAndGlyphs">INDIVIDUAL</text>
  <text class="node-label" x="570" y="1250" textLength="214" lengthAdjust="spacingAndGlyphs">VARIATION</text>

  <ellipse class="node" cx="565" cy="1528" rx="150" ry="93"/>
  <text class="node-label" x="565" y="1522" textLength="191" lengthAdjust="spacingAndGlyphs">NOMINAL</text>
  <text class="node-label" x="570" y="1575" textLength="80" lengthAdjust="spacingAndGlyphs">SIZE</text>

  <ellipse class="node" cx="996" cy="1528" rx="150" ry="93"/>
  <text class="node-label" x="996" y="1548" textLength="219" lengthAdjust="spacingAndGlyphs">BAREFOOT</text>

  <ellipse class="node" cx="1434" cy="1528" rx="150" ry="93"/>
  <text class="node-label" x="1433" y="1548" textLength="146" lengthAdjust="spacingAndGlyphs">HEIGHT</text>

  <ellipse class="node" cx="312" cy="1860" rx="150" ry="93"/>
  <text class="node-label" x="312" y="1815" textLength="118" lengthAdjust="spacingAndGlyphs">SHOD</text>
  <text class="node-label" x="312" y="1868" textLength="135" lengthAdjust="spacingAndGlyphs">TRACK</text>
  <text class="node-label" x="312" y="1920" textLength="162" lengthAdjust="spacingAndGlyphs">LENGTH</text>

  <ellipse class="node" cx="996" cy="1860" rx="150" ry="93"/>
  <text class="node-label small" x="996" y="1840" textLength="182" lengthAdjust="spacingAndGlyphs">BAREFOOT</text>
  <text class="node-label small" x="996" y="1893" textLength="257" lengthAdjust="spacingAndGlyphs">TRACK LENGTH</text>

  <!-- Relationship arrows -->
  <g class="link">
    <line class="rel" x1="490" y1="897" x2="810" y2="897"/>
    <polyline class="rel" points="518,867 488,897 518,928"/>
    <polyline class="rel" points="780,867 810,897 780,928"/>
    <circle class="badge-rel" cx="639" cy="894" r="31"/>
    <text class="badge-num" x="639" y="894">5</text>
  </g>

  <g class="link">
    <line class="rel" x1="294" y1="1042" x2="294" y2="1718"/>
    <polyline class="rel" points="263,1688 294,1719 325,1688"/>
    <circle class="badge-rel" cx="293" cy="1365" r="31"/>
    <text class="badge-num" x="293" y="1365">6</text>
  </g>

  <g class="link">
    <line class="rel" x1="657" y1="1437" x2="930" y2="1020"/>
    <polyline class="rel" points="888,1024 932,1016 941,1059"/>
    <circle class="badge-rel" cx="769" cy="1265" r="31"/>
    <text class="badge-num" x="769" y="1265">4</text>
  </g>

  <g class="link">
    <line class="rel" x1="1006" y1="1037" x2="1006" y2="1413"/>
    <polyline class="rel" points="975,1067 1006,1036 1037,1067"/>
    <polyline class="rel" points="975,1383 1006,1414 1037,1383"/>
    <circle class="badge-rel" cx="1006" cy="1222" r="31"/>
    <text class="badge-num" x="1006" y="1222">9</text>
  </g>

  <g class="link">
    <line class="rel" x1="730" y1="1530" x2="826" y2="1530"/>
    <polyline class="rel" points="797,1500 827,1530 797,1561"/>
    <circle class="badge-rel" cx="766" cy="1530" r="31"/>
    <text class="badge-num" x="766" y="1530">4</text>
  </g>

  <g class="link">
    <line class="rel" x1="1270" y1="1530" x2="1167" y2="1530"/>
    <polyline class="rel" points="1197,1500 1166,1530 1197,1561"/>
    <circle class="badge-rel" cx="1248" cy="1530" r="31"/>
    <text class="badge-num" x="1248" y="1530">8</text>
  </g>

  <g class="link">
    <line class="rel" x1="996" y1="1662" x2="996" y2="1733"/>
    <polyline class="rel" points="965,1703 996,1734 1027,1703"/>
    <circle class="badge-rel" cx="996" cy="1662" r="31"/>
    <text class="badge-num" x="996" y="1662">9</text>
  </g>

  <!-- Influence arrows -->
  <g class="link">
    <line class="inf" x1="1245" y1="897" x2="1167" y2="897"/>
    <polyline class="inf" points="1197,866 1166,897 1197,928"/>
    <circle class="badge-inf" cx="1250" cy="897" r="31"/>
    <text class="badge-num" x="1250" y="897">3</text>
  </g>

  <g class="link">
    <line class="inf" x1="478" y1="1110" x2="386" y2="1016"/>
    <polyline class="inf" points="383,1057 383,1013 427,1013"/>
    <circle class="badge-inf" cx="444" cy="1072" r="31"/>
    <text class="badge-num" x="444" y="1072">7</text>
  </g>

  <g class="link">
    <line class="inf" x1="702" y1="1135" x2="855" y2="983"/>
    <polyline class="inf" points="813,980 858,980 858,1025"/>
    <circle class="badge-inf" cx="755" cy="1080" r="31"/>
    <text class="badge-num" x="755" y="1080">7</text>
  </g>

  <g class="link">
    <line class="inf" x1="561" y1="1315" x2="561" y2="1418"/>
    <polyline class="inf" points="530,1388 561,1419 592,1388"/>
    <circle class="badge-inf" cx="561" cy="1355" r="31"/>
    <text class="badge-num" x="561" y="1355">5</text>
  </g>
</svg>
</body>
</html>
```